Flyer design for retail store owners

i would need to have a flyer design for my retail shop customers to show that I am a mailbox store that has all major shipping vendors to for their shipping needs. Ensuring that they can take advantage of opening a house account at the store and billed monthly, word document has all the details. Please use stock images for the notary public, passport photos, mailbox brass pictures of my actual mailboxes are listed in the pictures. I need to make it POP and WOW these retail store owners as I am using it to advertise the business

```html
<!DOCTYPE html>
<html lang="en">
<head>
<meta charset="utf-8">
<title>Swift Parcel &amp; Post – Mailbox Flyer</title>
<link href="https://fonts.googleapis.com/css2?family=Montserrat:wght@500;700;800;900&family=Open+Sans:ital,wght@0,400;0,600;0,700;1,600;1,700&display=swap" rel="stylesheet">
<style>
:root{
  --brown:#2e1d16;
  --red:#e42a1d;
  --orange:#e8411e;
  --green:#55892f;
  --green-light:#a9c486;
  --grey-band:#e3e6e0;
  --grey-text:#8c8c8c;
  --ink:#1f1f1f;
  --bg:#e4e6ea;
  --white:#ffffff;
  --tan:#c9a06a;
}
*{box-sizing:border-box;margin:0;padding:0}
html,body{width:956px;height:1200px;overflow:hidden;background:var(--bg)}
body{position:relative;font-family:'Open Sans',Arial,sans-serif;color:var(--ink)}
.page{position:absolute;top:301px;width:592px;height:767px;background:var(--white);transform-origin:0 0;transform:scale(.78);overflow:hidden;box-shadow:0 2px 6px rgba(0,0,0,.15)}
.page--front{left:10px}
.page--back{left:484px}
.abs{position:absolute}
.head{font-family:'Montserrat',Arial,sans-serif;font-weight:800;line-height:1.02;text-transform:uppercase}
.photo{position:absolute}
.circle{border-radius:50%;border:3px solid #fff;box-shadow:0 2px 5px rgba(0,0,0,.35)}

/* front */
.masthead{left:0;top:0;width:592px;height:120px;background:var(--brown)}
.brand-box{left:26px;top:26px;width:194px;height:68px;background:var(--red);display:flex;align-items:center;justify-content:center;text-align:center;color:#fff;font-family:'Montserrat',sans-serif;font-weight:900;font-size:21px;line-height:1.1}
.title{left:246px;top:30px;color:#fff;font-size:31px;font-weight:900}
.title-sub{left:246px;top:88px;color:var(--orange);font-family:'Montserrat',sans-serif;font-weight:700;font-size:8.5px;text-transform:uppercase}
.hero-icon{left:464px;top:30px;width:108px;height:68px;background:linear-gradient(135deg,#6a9b45,#3e7425);border:2px solid #fff;border-radius:4px}
.mailbox-photo{left:306px;top:108px;width:262px;height:292px;background:linear-gradient(135deg,#dcb783,#b88954 60%,#9d7243)}
.grey-band{left:0;top:305px;width:592px;height:100px;background:var(--grey-band)}
.intro-h{left:26px;top:140px;color:var(--green);font-size:17px}
.intro-p{left:26px;top:159px;width:270px;color:var(--grey-text);font-family:'Montserrat',sans-serif;font-weight:700;font-size:10.4px;line-height:1.3;text-transform:uppercase}
.intro-h2{left:26px;top:203px;width:280px;font-size:17px;color:var(--ink)}
.intro-h2 span{color:var(--red)}
.intro-p2{top:258px}
.notice{left:26px;top:312px;width:250px;font-style:italic;font-weight:700;font-size:10px;line-height:1.32}
.promo{left:276px;top:266px;width:160px;height:160px}
.promo-text{left:276px;top:302px;width:160px;text-align:center;color:#fff;font-family:'Montserrat',sans-serif}
.promo-text .l1{font-weight:900;font-size:17px;line-height:1}
.promo-text .l2{font-weight:500;font-size:13px;line-height:1.1}
.promo-text .price{font-weight:900;font-size:44px;line-height:1}
.promo-text .price small{font-size:12px;vertical-align:top}
.promo-text .price em{font-style:normal;font-size:13px;font-weight:700}
.promo-text .l3{font-size:8.5px;font-weight:500}
.offer-h{left:26px;top:414px;color:var(--green);font-size:17px}
.offer-rule{left:124px;top:418px;width:1.5px;height:30px;background:var(--ink)}
.offer-note{left:134px;top:418px;width:215px;font-size:8.6px;line-height:1.3}
.list{font-size:8.6px;line-height:16px;list-style:none}
.list li{display:flex;align-items:center;gap:5px;white-space:nowrap}
.list svg{flex:none}
.offer-a{left:26px;top:455px}
.offer-b{left:188px;top:455px}
.signup{left:26px;top:497px;width:320px;height:28px;background:var(--brown);padding:3px}
.signup-inner{width:100%;height:100%;background:var(--green-light);display:flex;align-items:center;padding-left:7px;font-family:'Montserrat',sans-serif;font-weight:800;font-size:11.5px;color:var(--brown)}
.signup-inner b{margin-left:auto;background:var(--brown);color:var(--green-light);height:100%;display:flex;align-items:center;padding:0 6px;font-weight:900;font-size:15px}
.services-h{left:26px;top:531px;font-size:15.5px;color:var(--ink)}
.services-h span{color:var(--red)}
.service{font-size:9px;display:flex;align-items:center;gap:9px}
.footer{left:0;top:733px;width:386px;height:34px}
.footer-text{left:28px;top:743px;display:flex;gap:16px;color:#fff;font-family:'Montserrat',sans-serif;font-weight:700;font-size:10.5px}
.footer-text span{display:flex;align-items:center;gap:6px}
.deals-h{left:360px;top:418px;font-size:15.5px}
.deals-h span{color:var(--red)}
.deals-rule{left:360px;top:464px;width:185px;height:1.5px;background:var(--red)}
.deals{left:360px;top:480px;width:200px;list-style:none;font-size:7.8px;line-height:1.38}
.deals li{display:flex;gap:6px;margin-bottom:8px}
.deals svg{flex:none;margin-top:1px}
.contact-bar{height:20px;background:var(--green-light);border-left:4px solid var(--brown);font-family:'Montserrat',sans-serif;font-weight:800;font-size:10.5px;color:var(--brown);padding-left:18px;display:flex;align-items:center}
.call-us{font-family:'Montserrat',sans-serif;color:var(--green);font-weight:800;font-size:13px;line-height:.95}
.call-us span{display:block;color:var(--orange);font-weight:500}
.phone{display:flex;align-items:center;gap:6px;font-family:'Montserrat',sans-serif;font-weight:500;font-size:17px}
.small-line{display:flex;align-items:center;gap:5px;font-size:9.2px;font-weight:600}

/* back */
.topbar{left:0;top:0;width:592px;height:12px;background:var(--brown)}
.back-h{left:0;top:36px;width:592px;text-align:center;color:var(--red);font-size:25.5px;font-weight:900}
.back-band{left:0;top:97px;width:592px;height:29px;background:var(--grey-band);text-align:center;font-size:19px;font-weight:800;line-height:29px;color:var(--ink)}
.ticks{left:0;width:592px;display:flex;justify-content:center;gap:22px;font-family:'Montserrat',sans-serif;font-weight:700;font-size:14px}
.ticks span{display:flex;align-items:center;gap:8px}
.help{left:0;top:225px;width:592px;height:165px;background:var(--green)}
.help-frame{left:16px;top:251px;width:560px;height:124px;border:1px solid rgba(255,255,255,.45)}
.help-h{left:0;top:238px;width:592px;text-align:center;color:#fff;font-size:27px;font-weight:900}
.help-h b{background:var(--green);padding:0 8px;font-weight:900}
.help-p{left:30px;top:285px;width:532px;text-align:center;color:#fff;font-family:'Montserrat',sans-serif;font-weight:500;font-size:15.3px;line-height:1.4;text-transform:uppercase}
.help-rule{left:246px;top:374px;width:100px;height:2px;background:#fff}
.sp-h{left:0;top:570px;width:592px;text-align:center;color:var(--red);font-size:25px;font-weight:800}
.sp-rule{top:586px;width:138px;height:2px;background:var(--red)}
.badge{top:612px;height:38px;border-radius:3px}
</style>
</head>
<body>

<!-- FRONT PAGE -->
<section class="page page--front">
  <div class="abs masthead"></div>
  <div class="abs brand-box">SWIFT PARCEL<br>&amp; POST</div>
  <h1 class="abs head title">Renting<br>Mailboxes</h1>
  <p class="abs title-sub">On Maple Ridge Shopping Center</p>
  <div class="photo hero-icon" role="img" aria-label="Illustration of a parcel box under a magnifying glass"></div>

  <div class="abs grey-band"></div>
  <div class="photo mailbox-photo" role="img" aria-label="Photo of a brass mailbox wall cabinet"></div>

  <h2 class="abs head intro-h">Renting a mail box</h2>
  <p class="abs intro-p">Is one of the most efficient and cost saving methods for receiving your mail and packages.</p>
  <h2 class="abs head intro-h2"><span>Private security, weather conditions,</span> sorting, and deliveries</h2>
  <p class="abs intro-p intro-p2">All you have to do is pick-up your mail from our secured facility each day except Sundays.</p>
  <p class="abs notice">You will get a notification when mail arrives whether envelope or package, it will be scanned in daily which other mailbox stores do not offer. We offer onsite Notary Public with no appointments and onsite Passport Photos and can ship out same day.</p>

  <svg class="abs promo" viewBox="0 0 160 160" aria-hidden="true">
    <polygon fill="#fff" points="80,0 89,12 102,3 107,18 122,13 123,28 139,27 135,42 150,45 142,58 155,66 144,77 154,89 140,95 146,109 131,111 133,127 118,125 114,141 101,134 92,148 82,137 72,149 64,135 50,142 47,127 31,129 33,114 18,110 25,96 11,88 22,77 10,66 24,59 17,45 32,42 29,27 44,28 46,13 61,18 67,4"/>
    <polygon fill="#e8411e" points="80,5 88,16 100,8 105,22 119,18 120,32 134,32 131,45 145,48 137,60 149,67 139,77 148,88 135,93 141,106 127,108 128,123 114,121 111,136 99,130 91,143 82,133 73,144 65,131 52,138 49,124 35,126 37,112 23,108 30,95 17,88 27,78 16,67 29,61 22,48 36,45 34,31 48,32 49,18 63,23 69,9"/>
  </svg>
  <div class="abs promo-text">
    <div class="l1">EXCLUSIVE</div>
    <div class="l2">PROMO DEAL</div>
    <div class="price"><small>$</small>12<em>FOR</em></div>
    <div class="l3">6-12 MONTHS LEASES</div>
  </div>

  <h2 class="abs head offer-h">We are<br>offering</h2>
  <div class="abs offer-rule"></div>
  <p class="abs offer-note">All Maple Ridge shopping center owners or employees an exclusive promo deal.</p>
  <ul class="abs list offer-a">
    <li><svg width="8" height="8" viewBox="0 0 10 10"><circle cx="5" cy="5" r="4" fill="none" stroke="#e42a1d" stroke-width="1.2"/><path d="M3 5l1.5 1.5L7 3.5" fill="none" stroke="#e42a1d" stroke-width="1.2"/></svg>Book of stamps(20 count)</li>
    <li><svg width="8" height="8" viewBox="0 0 10 10"><circle cx="5" cy="5" r="4" fill="none" stroke="#e42a1d" stroke-width="1.2"/><path d="M3 5l1.5 1.5L7 3.5" fill="none" stroke="#e42a1d" stroke-width="1.2"/></svg>100 copies of black and white</li>
  </ul>
  <ul class="abs list offer-b">
    <li><svg width="8" height="8" viewBox="0 0 10 10"><circle cx="5" cy="5" r="4" fill="none" stroke="#e42a1d" stroke-width="1.2"/><path d="M3 5l1.5 1.5L7 3.5" fill="none" stroke="#e42a1d" stroke-width="1.2"/></svg>3 notarizations by appointment</li>
    <li><svg width="8" height="8" viewBox="0 0 10 10"><circle cx="5" cy="5" r="4" fill="none" stroke="#e42a1d" stroke-width="1.2"/><path d="M3 5l1.5 1.5L7 3.5" fill="none" stroke="#e42a1d" stroke-width="1.2"/></svg>100 copies of color</li>
  </ul>

  <div class="abs signup"><div class="signup-inner">PLEASE SEE ASSOCIATE FOR <b>SIGN UP</b></div></div>
  <h2 class="abs head services-h"><span>Our services</span> included</h2>

  <div class="abs service" style="left:26px;top:565px">
    <svg width="20" height="22" viewBox="0 0 20 22" fill="none" stroke="#333" stroke-width="1.3"><rect x="2" y="2" width="13" height="18"/><path d="M5 7h7M5 11h7M5 15h4M13 17l5-9 1.5 1-5 9z"/></svg>Notary</div>
  <div class="abs service" style="left:150px;top:565px">
    <svg width="26" height="20" viewBox="0 0 26 20" fill="none" stroke="#333" stroke-width="1.3"><rect x="1" y="3" width="22" height="15"/><path d="M1 3l11 9 11-9"/></svg>Mailbox Rental Service</div>
  <div class="abs service" style="left:26px;top:600px">
    <svg width="20" height="22" viewBox="0 0 20 22" fill="none" stroke="#333" stroke-width="1.3"><rect x="2" y="1" width="16" height="20"/><circle cx="10" cy="10" r="5"/><path d="M5 10h10M10 5v10"/></svg>Passport photos</div>
  <div class="abs service" style="left:150px;top:600px">
    <svg width="26" height="20" viewBox="0 0 26 20" fill="none" stroke="#333" stroke-width="1.3"><path d="M13 2l10 4-10 4L3 6zM3 6v8l10 4 10-4V6M13 10v8"/></svg>Packing Materials</div>

  <div class="photo circle" style="left:27px;top:628px;width:98px;height:98px;background:radial-gradient(circle at 40% 40%,#2a3f7a,#121d45)" role="img" aria-label="Photo of a passport cover"></div>
  <div class="photo circle" style="left:124px;top:628px;width:98px;height:98px;background:linear-gradient(160deg,#d8e2ef,#5d7fa8 60%,#27364d)" role="img" aria-label="Photo of a hand using a copy machine"></div>
  <div class="photo circle" style="left:222px;top:628px;width:98px;height:98px;background:linear-gradient(135deg,#cdb08a,#7a5a3c)" role="img" aria-label="Photo of an open brass mailbox door"></div>

  <svg class="abs footer" viewBox="0 0 386 34" preserveAspectRatio="none" aria-hidden="true"><path d="M0 0H366Q386 0 386 20V34H0z" fill="#55892f"/></svg>
  <div class="abs footer-text">
    <span><svg width="11" height="11" viewBox="0 0 12 12"><circle cx="6" cy="6" r="6" fill="#e42a1d"/><circle cx="6" cy="6" r="3.3" fill="none" stroke="#fff"/><path d="M2.7 6h6.6M6 2.7v6.6" stroke="#fff"/></svg>SWIFTPARCELPOST.NET</span>
    <span><svg width="11" height="11" viewBox="0 0 12 12"><circle cx="6" cy="6" r="6" fill="#e42a1d"/><rect x="3" y="3.5" width="6" height="5" fill="#fff"/></svg>555-014-3390</span>
  </div>

  <h2 class="abs head deals-h"><span>Check out these</span><br>other deals</h2>
  <div class="abs deals-rule"></div>
  <ul class="abs deals">
    <li><svg width="8" height="8" viewBox="0 0 10 10"><circle cx="5" cy="5" r="4" fill="none" stroke="#55892f" stroke-width="1.2"/><path d="M3 5l1.5 1.5L7 3.5" fill="none" stroke="#55892f" stroke-width="1.2"/></svg><span>As a retail owner, you know how important it is to keep your customers coming back - <b>you will get 20% discount for printing services.</b></span></li>
    <li><svg width="8" height="8" viewBox="0 0 10 10"><circle cx="5" cy="5" r="4" fill="none" stroke="#55892f" stroke-width="1.2"/><path d="M3 5l1.5 1.5L7 3.5" fill="none" stroke="#55892f" stroke-width="1.2"/></svg><span>We <b>duplicate keys for $2/each,</b> our regular price charge is $4/each. <b>Save up to 50%.</b></span></li>
    <li><svg width="8" height="8" viewBox="0 0 10 10"><circle cx="5" cy="5" r="4" fill="none" stroke="#55892f" stroke-width="1.2"/><path d="M3 5l1.5 1.5L7 3.5" fill="none" stroke="#55892f" stroke-width="1.2"/></svg><span><b>Lamination</b> is also discounted at <b>10% off.</b></span></li>
    <li><svg width="8" height="8" viewBox="0 0 10 10"><circle cx="5" cy="5" r="4" fill="none" stroke="#55892f" stroke-width="1.2"/><path d="M3 5l1.5 1.5L7 3.5" fill="none" stroke="#55892f" stroke-width="1.2"/></svg><span><b>10% off retail supplies</b> ... must be minimum of 10$</span></li>
    <li><svg width="8" height="8" viewBox="0 0 10 10"><circle cx="5" cy="5" r="4" fill="none" stroke="#55892f" stroke-width="1.2"/><path d="M3 5l1.5 1.5L7 3.5" fill="none" stroke="#55892f" stroke-width="1.2"/></svg><span>For house accounts - a 5% discount will be deducted monthly of billing change to invoicing PLUS we're giving another <b>5% of the discount if you upgrade and sign up for mailbox.</b> Great right?</span></li>
  </ul>

  <div class="abs contact-bar" style="left:440px;top:660px;width:152px">CONTACT US</div>
  <div class="abs call-us" style="left:378px;top:693px">CALL US<span>TODAY</span></div>
  <div class="abs phone" style="left:436px;top:690px"><svg width="22" height="22" viewBox="0 0 22 22"><circle cx="11" cy="11" r="10" fill="none" stroke="#e42a1d" stroke-width="1.5"/><path d="M7 6c-1 1-1 3 1 6s4 4 6 4l1.5-1.5-2-2-1.3.8c-1-.5-2.2-1.8-2.8-2.8l.8-1.3-2-2z" fill="#e42a1d"/></svg>555-014-2277</div>
  <div class="abs small-line" style="left:363px;top:724px"><svg width="10" height="12" viewBox="0 0 10 12"><path d="M5 11C2 7 1 5.5 1 4a4 4 0 018 0c0 1.5-1 3-4 7z" fill="#e42a1d"/><circle cx="5" cy="4" r="1.5" fill="#fff"/></svg>214 Harbor Ave Easton, NY 10000-1234</div>
  <div class="abs small-line" style="left:535px;top:746px;transform:translateX(-100%);margin-left:40px"><svg width="11" height="11" viewBox="0 0 12 12"><circle cx="6" cy="6" r="6" fill="#e42a1d"/><rect x="3" y="4" width="6" height="4" fill="#fff"/></svg>hello@swiftparcelpost.net</div>
</section>

<!-- BACK PAGE -->
<section class="page page--back">
  <div class="abs topbar"></div>
  <h2 class="abs head back-h">We are ready to handle all<br>of your postal services</h2>
  <div class="abs back-band head">Get also the services you need</div>

  <div class="abs ticks" style="top:148px">
    <span><svg width="12" height="12" viewBox="0 0 10 10"><circle cx="5" cy="5" r="4" fill="none" stroke="#55892f" stroke-width="1"/><path d="M3 5l1.5 1.5L7 3.5" fill="none" stroke="#55892f" stroke-width="1"/></svg>Printing</span>
    <span><svg width="12" height="12" viewBox="0 0 10 10"><circle cx="5" cy="5" r="4" fill="none" stroke="#55892f" stroke-width="1"/><path d="M3 5l1.5 1.5L7 3.5" fill="none" stroke="#55892f" stroke-width="1"/></svg>Shipping materials.</span>
    <span><svg width="12" height="12" viewBox="0 0 10 10"><circle cx="5" cy="5" r="4" fill="none" stroke="#55892f" stroke-width="1"/><path d="M3 5l1.5 1.5L7 3.5" fill="none" stroke="#55892f" stroke-width="1"/></svg>Copying</span>
  </div>
  <div class="abs ticks" style="top:183px">
    <span><svg width="12" height="12" viewBox="0 0 10 10"><circle cx="5" cy="5" r="4" fill="none" stroke="#55892f" stroke-width="1"/><path d="M3 5l1.5 1.5L7 3.5" fill="none" stroke="#55892f" stroke-width="1"/></svg>Stop in to purchase postage</span>
  </div>

  <div class="abs help"></div>
  <div class="abs help-frame"></div>
  <h2 class="abs head help-h"><b>We are here to help</b></h2>
  <p class="abs help-p">At Swift Parcel &amp; Post, our goal is to make your shipping experience as convenient as possible. Whether you are shipping packages, documents, or packages,</p>
  <div class="abs help-rule"></div>

  <div class="photo circle" style="left:58px;top:410px;width:145px;height:145px;background:linear-gradient(135deg,#e9e9ea,#6d7d98 55%,#2d3a55)" role="img" aria-label="Photo of a courier loading parcels into a delivery truck"></div>
  <div class="photo circle" style="left:222px;top:410px;width:145px;height:145px;background:linear-gradient(160deg,#e8ecf1,#9fb3cc 50%,#5b6f8a)" role="img" aria-label="Photo of a cargo plane flying above the clouds"></div>
  <div class="photo circle" style="left:385px;top:410px;width:145px;height:145px;background:linear-gradient(135deg,#e7c79c,#c99a62)" role="img" aria-label="Photo of corrugated cardboard sheets"></div>

  <div class="abs sp-rule" style="left:30px"></div>
  <h2 class="abs head sp-h">Service point</h2>
  <div class="abs sp-rule" style="left:424px"></div>

  <div class="abs badge" style="left:30px;width:96px;background:#d9d6d2"></div>
  <div class="abs badge" style="left:150px;width:115px;background:#ece7f2"></div>
  <div class="abs badge" style="left:289px;width:125px;background:#dde4f0"></div>
  <div class="abs badge" style="left:440px;width:126px;background:#fcce0a"></div>

  <div class="abs contact-bar" style="left:440px;top:668px;width:152px">CONTACT US</div>
  <div class="abs call-us" style="left:30px;top:694px;font-size:15px">CALL US<span>TODAY</span></div>
  <div class="abs phone" style="left:104px;top:690px;font-size:21px"><svg width="26" height="26" viewBox="0 0 22 22"><circle cx="11" cy="11" r="10" fill="none" stroke="#e42a1d" stroke-width="1.5"/><path d="M7 6c-1 1-1 3 1 6s4 4 6 4l1.5-1.5-2-2-1.3.8c-1-.5-2.2-1.8-2.8-2.8l.8-1.3-2-2z" fill="#e42a1d"/></svg>555-014-2277</div>
  <div class="abs small-line" style="left:405px;top:708px"><svg width="11" height="11" viewBox="0 0 12 12"><circle cx="6" cy="6" r="6" fill="#e42a1d"/><rect x="3" y="4" width="6" height="4" fill="#fff"/></svg>hello@swiftparcelpost.net</div>
  <div class="abs small-line" style="left:345px;top:727px"><svg width="10" height="12" viewBox="0 0 10 12"><path d="M5 11C2 7 1 5.5 1 4a4 4 0 018 0c0 1.5-1 3-4 7z" fill="#e42a1d"/><circle cx="5" cy="4" r="1.5" fill="#fff"/></svg>214 Harbor Ave Easton, NY 10000-1234</div>

  <svg class="abs footer" viewBox="0 0 386 34" preserveAspectRatio="none" aria-hidden="true"><path d="M0 0H366Q386 0 386 20V34H0z" fill="#55892f"/></svg>
  <div class="abs footer-text">
    <span><svg width="11" height="11" viewBox="0 0 12 12"><circle cx="6" cy="6" r="6" fill="#e42a1d"/><circle cx="6" cy="6" r="3.3" fill="none" stroke="#fff"/><path d="M2.7 6h6.6M6 2.7v6.6" stroke="#fff"/></svg>SWIFTPARCELPOST.NET</span>
    <span><svg width="11" height="11" viewBox="0 0 12 12"><circle cx="6" cy="6" r="6" fill="#e42a1d"/><rect x="3" y="3.5" width="6" height="5" fill="#fff"/></svg>555-014-3390</span>
  </div>
</section>

</body>
</html>
```